Real Estate Open House & For Sale Signage

I am designing brand new signs for my real estate company. All I have so far are my logo and a business card design. I would like to have designed two different signs, 1. Open House directional sign, 2. For Sale Company sign. Both signs need to will be eye catching from the street, easy to read, identifiable and memorable.

Target Market(s)

Males & females, Ages between 30-65, affluent, educated, professionals.

Industry/Entity Type

Real Estate

Font styles to use
Serif
Sans Serif

Colors
33b8a4
34a7d8
acd137
3277b5

Requirements
Must have
• Must have my company logo & real estate license number visible on the sign. Must be easily visible and eye catching from a moving vehicle. Must have a professional and trustworthy appeal. Must bring to mind real estate.
Nice to have
• Image or icon that will denote real estate and be known as a part of my company identity and marketing theme.
Should not have
• Attached is a feeble attempt at creating my For Sale sign. The information on the sign is accurate, but the design is not appealing to me at all. It feels very amateurish.

```html
<!DOCTYPE html>
<html lang="en">
<head>
<meta charset="utf-8">
<title>For Sale Sign</title>
<link href="https://fonts.googleapis.com/css2?family=Tinos:wght@400;700&display=swap" rel="stylesheet">
<style>
  :root {
    --sign-white: #ffffff;
    --brand-green: #a6cf3a;
    --band-grey: #5b5b5d;
    --ink-grey: #4a4a4a;
    --rule-grey: #555555;
  }
  html, body {
    margin: 0;
    padding: 0;
    width: 1200px;
    height: 1030px;
    overflow: hidden;
    background: var(--sign-white);
  }
  .sign {
    position: relative;
    width: 1200px;
    height: 1030px;
    background: var(--sign-white);
    font-family: "Tinos", "Times New Roman", serif;
    overflow: hidden;
  }
  .sign-shapes {
    position: absolute;
    inset: 0;
  }
  .headline {
    position: absolute;
    left: 0;
    right: 0;
    top: 62px;
    margin: 0;
    text-align: center;
    font-size: 180px;
    line-height: 1;
    font-weight: 700;
    color: var(--brand-green);
  }
  .tagline {
    position: absolute;
    left: 0;
    right: 0;
    top: 266px;
    margin: 0;
    text-align: center;
    font-size: 38px;
    line-height: 1;
    font-weight: 400;
    color: var(--ink-grey);
    letter-spacing: 7px;
  }
  .company-name {
    position: absolute;
    left: 0;
    right: 0;
    top: 528px;
    text-align: center;
    color: var(--brand-green);
    font-weight: 700;
    line-height: 1.05;
  }
  .company-name .primary {
    display: block;
    font-size: 72px;
    letter-spacing: 8px;
  }
  .company-name .secondary {
    display: block;
    font-size: 30px;
    letter-spacing: 5px;
  }
  .agent-name {
    position: absolute;
    left: 0;
    right: 0;
    top: 792px;
    text-align: center;
    font-size: 54px;
    line-height: 1;
    color: var(--sign-white);
  }
  .agent-phone {
    position: absolute;
    left: 0;
    right: 0;
    top: 882px;
    display: flex;
    justify-content: center;
    align-items: center;
    gap: 70px;
    color: var(--sign-white);
    font-size: 118px;
    font-weight: 700;
    line-height: 1;
  }
  .phone-icon {
    width: 100px;
    height: 100px;
  }
</style>
</head>
<body>
  <div class="sign">
    <svg class="sign-shapes" width="1200" height="1030" viewBox="0 0 1200 1030">
      <path class="divider-rule" d="M130,368 Q600,372 1080,400" fill="none" stroke="var(--rule-grey)" stroke-width="2"/>
      <path class="contact-band" d="M0,612 C330,780 800,800 1200,552 L1200,1030 L0,1030 Z" fill="var(--band-grey)"/>
      <path class="accent-swoosh" d="M580,764 C860,770 1100,640 1200,448 L1200,520 C1080,700 850,780 580,764 Z" fill="var(--brand-green)"/>
    </svg>

    <h1 class="headline">FOR SALE</h1>
    <p class="tagline">YOUR NEIGHBORHOOD SPECIALIST</p>

    <div class="company-name">
      <span class="primary">KAILUA</span>
      <span class="secondary">HOME PARTNERS LLC</span>
    </div>

    <div class="agent-name">Leila Torres</div>

    <div class="agent-phone">
      <svg class="phone-icon" viewBox="0 0 100 100" aria-hidden="true">
        <circle cx="50" cy="50" r="44" fill="none" stroke="var(--sign-white)" stroke-width="7"/>
        <path d="M34,24 L42,22 L48,38 L42,43 C45,52 50,58 58,62 L63,56 L78,63 L76,71 C73,77 66,79 58,76 C42,69 31,57 25,42 C23,34 27,27 34,24 Z" fill="var(--sign-white)"/>
      </svg>
      <span class="phone-number">(808) 555-0142</span>
    </div>
  </div>
</body>
</html>
```